Eye-catching Yellow Page Ad for Attorney's Office

We need a phone book advertisement for our law office. We practice workers' compensation law, and our clientele consists exclusively of individuals who have been injured on the job. The dimensions of the print ad will be 6" W X 4.54" H.

We've had our current ad for several years, and wanted to get a new one that has been designed by a professional. Being that it's an ad for a law firm, it needs to be professional looking, but we're hoping to have something that looks a little more modern and has eye-catching appeal. We like the text that is included in the ad, and we want to make sure our phone number is very visible. No real preference for color scheme.

I've attached a copy of our current ad. All the information included in there is accurate. Our office name is Thornbury & Lisle, PLLC. The ethical rules for attorney advertising require the PLLC to be included in the ad, but it can be smaller than the other text (see our current ad).

Target Market(s)

Our potential clients are injured workers looking for legal representation in their workers' compensation claim.

Industry/Entity Type

Attorney

Font styles to use
Serif
Sans Serif

Requirements
Must have
• Professional, but stands out from the crowd
Nice to have
• Clean modern design
Should not have
• We don't want it to be too crowded or over-worked.

```html
<!DOCTYPE html>
<html lang="en">
<head>
<meta charset="utf-8">
<title>Thornbury &amp; Lisle, PLLC</title>
<link rel="stylesheet" href="https://fonts.googleapis.com/css2?family=Libre+Baskerville:wght@400;700&family=Tinos:wght@700&family=Questrial&family=Oswald:wght@500&family=Archivo:wght@700&family=Poppins:wght@600&display=swap">
<style>
  :root {
    --stage: #1a0f08;
    --wood-dark: #2a1408;
    --wood-mid: #6b3512;
    --wood-light: #b5692a;
    --gold: #f2b25a;
    --gold-soft: #e9a356;
    --cream: #f6e6c4;
    --band: rgba(20, 8, 2, 0.55);
    --band-deep: rgba(10, 4, 0, 0.7);
    --frame: #d8c9a0;
  }
  * { margin: 0; padding: 0; box-sizing: border-box; }
  html, body { width: 1200px; height: 1000px; overflow: hidden; background: var(--stage); }
  .canvas { position: relative; width: 1200px; height: 1000px; background: var(--stage); }
  .ad {
    position: absolute; left: 32px; top: 75px; width: 1126px; height: 850px; overflow: hidden;
    background:
      radial-gradient(ellipse at 50% 35%, rgba(230,150,70,0.55), transparent 60%),
      linear-gradient(90deg, var(--wood-dark) 0%, var(--wood-mid) 35%, var(--wood-light) 55%, var(--wood-mid) 80%, var(--wood-dark) 100%);
  }
  .scales-art {
    position: absolute; left: 720px; top: 10px; width: 406px; height: 420px;
    background: radial-gradient(ellipse at 45% 55%, rgba(200,140,70,0.85), rgba(110,60,20,0.4) 60%, transparent 80%);
  }
  .firm-name {
    position: absolute; left: 40px; top: 68px; width: 620px; text-align: center;
    font-family: "Libre Baskerville", serif; font-weight: 400; color: var(--gold);
  }
  .firm-name .name { font-size: 58px; line-height: 1; }
  .firm-name .suffix { font-size: 15px; letter-spacing: 1px; margin-top: 12px; }
  .intro {
    position: absolute; left: 20px; top: 210px; width: 680px; text-align: center;
    font-family: "Tinos", serif; font-weight: 700; font-size: 23px; line-height: 38px;
    letter-spacing: 1.5px; color: var(--gold-soft);
  }
  .credential {
    position: absolute; left: 20px; top: 347px; width: 680px; text-align: center;
    font-family: "Poppins", sans-serif; font-weight: 600; font-size: 27px; line-height: 40px;
    color: var(--cream);
  }
  .services-band { position: absolute; left: 0; top: 453px; width: 1126px; height: 302px; background: var(--band); }
  .contact-band { position: absolute; left: 0; top: 755px; width: 1126px; height: 95px; background: var(--band-deep); }
  .values {
    position: absolute; left: 58px; top: 474px;
    font-family: "Oswald", sans-serif; font-weight: 500; font-size: 29px; letter-spacing: 0.5px; color: var(--gold);
  }
  .help-title {
    position: absolute; left: 146px; top: 528px;
    font-family: "Libre Baskerville", serif; font-weight: 700; font-size: 30px; color: var(--cream);
  }
  .service-list {
    position: absolute; top: 584px; list-style: none;
    font-family: "Questrial", sans-serif; font-size: 23px; line-height: 32px; color: var(--gold-soft);
  }
  .service-list li::before { content: "•"; margin-right: 9px; color: var(--cream); }
  .service-list.col-a { left: 30px; }
  .service-list.col-b { left: 414px; }
  .team-photo {
    position: absolute; left: 786px; top: 462px; width: 296px; height: 272px;
    border: 4px solid var(--frame);
    background: linear-gradient(180deg, #8a5a3a 0%, #5a3a2a 45%, #2c1f1a 100%);
  }
  .phone {
    position: absolute; left: 36px; top: 772px;
    font-family: "Libre Baskerville", serif; font-weight: 700; font-size: 52px; letter-spacing: 3px; color: var(--gold);
  }
  .address {
    position: absolute; right: 34px; top: 770px; text-align: right;
    font-family: "Archivo", sans-serif; font-weight: 700; font-size: 22px; line-height: 38px;
    letter-spacing: 1.5px; color: var(--gold);
  }
</style>
</head>
<body>
<div class="canvas">
  <section class="ad">
    <div class="scales-art" role="img" aria-label="Brass scales of justice on a courtroom bench"></div>

    <header class="firm-name">
      <div class="name">Thornbury &amp; Lisle</div>
      <div class="suffix">PLLC</div>
    </header>

    <p class="intro">At Thornbury &amp; Lisle, We Provide Personal<br>Attention To Out Clients.That Means Your Case<br>Is Handled By An Attorney, Not An Assistant.</p>

    <p class="credential">Former Assistant Attorneys General<br>Who Know The System</p>

    <div class="services-band"></div>
    <div class="contact-band"></div>

    <p class="values">PROFESSIONAL • COMMITTED • EFFECTIVE</p>
    <h2 class="help-title">We Can Help With:</h2>

    <ul class="service-list col-a">
      <li>Workplace Injuries Or Death</li>
      <li>Lost Wages</li>
      <li>Medical Expenses &amp; Treatment</li>
      <li>Hearing Loss Claims</li>
    </ul>
    <ul class="service-list col-b">
      <li>Pension Claims</li>
      <li>Disability Awards</li>
      <li>Return To Work Issues</li>
    </ul>

    <div class="team-photo" role="img" aria-label="Portrait of the two attorneys in a law library"></div>

    <p class="phone">360 555-0147</p>
    <p class="address">www.thornburylisle.com<br>402 W Harbor St Suite 310, Fairhaven</p>
  </section>
</div>
</body>
</html>
```